Kx7Orbit WebSite

an educational website about tutoring, client will be surfing this site looking for a tutor, please see the attached images because the contains exactly what we need.
Updates

Project Deadline Extended Reason: something went wrong with the uploaded files, we are very sorry.thank you PlumeVault for the 5 days extension.now there is a 3 images describing the content of the three pages.good luck Added Friday, August 5, 2016

Target Market(s)

everyone

Industry/Entity Type

Education

Number of Pages Required

3 page

Font styles to use
Other font styles liked:
• something looks good in Arabic and english like "Droid Arabic Kufi"

Requirements
Must have
• the logo we attached, responsive design, simple, also try as much as you can Centering texts and layout because this website will have an Arabic version, Arabic is a Right-to-Left Language.
• a change language button,
Nice to have
• educational gestures.
• Centered texts and layout because this website will have an Arabic version, Arabic is a Right-to-Left Language.
• we have a web designer and we can download any template and add our logo and text to it, but.....
• we need creativity, so please stick to the contents in the images we attached, we need something very simple, more like a zorvia home page with little touch of filtering fields like the 5 dropdownlist and the gender selection buttons.
• try not to go far away from the contents we specified in the images, use less images or dont use images at all, try not to make the client scroll down,
Should not have
• too much colors or noisy layout or heavy media

```html
<!DOCTYPE html>
<html lang="en">
<head>
<meta charset="utf-8">
<title>Kx7Orbit – Search Result</title>
<link href="https://fonts.googleapis.com/css2?family=Montserrat:wght@300;400;500;700&family=Open+Sans:wght@400;600&display=swap" rel="stylesheet">
<style>
:root{
  --navy:#082a44;
  --orange:#f36f21;
  --orange-dark:#d95f16;
  --blue:#1a78c2;
  --logo-blue:#2a9be0;
  --ink:#173247;
  --note:#f8e49c;
  --note-light:#fbedb9;
  --footer:#262626;
  --footer-bottom:#1e1e1e;
  --footer-line:#3c3c3c;
  --white:#ffffff;
  --muted:#6a6a6a;
}
*{margin:0;padding:0;box-sizing:border-box}
html,body{width:1200px;height:952px;overflow:hidden;background:var(--white)}
body{position:relative;font-family:"Montserrat",sans-serif;color:var(--ink)}
.abs{position:absolute}

/* header */
.site-header{left:0;top:0;width:1200px;height:104px;background:var(--navy)}
.brand{left:131px;top:30px;display:flex;align-items:center;gap:8px}
.brand-mark{width:26px;height:26px;background:var(--logo-blue);border-radius:4px}
.brand-name{font-family:"Montserrat",sans-serif;font-weight:700;font-size:29px;color:var(--logo-blue);letter-spacing:-.5px}
.lang-switch{right:152px;top:16px;display:flex;align-items:center;gap:10px;color:#b8c6d2;font-size:11px}
.lang-switch .ar{font-size:17px;font-weight:700;color:var(--white)}
.main-nav{left:410px;top:55px;display:flex;gap:45px}
.main-nav a{color:var(--white);text-decoration:none;font-size:17px;font-weight:400}
.auth{top:48px;height:34px;border:2px solid var(--white);border-radius:3px;color:var(--white);font-size:14px;font-weight:500;display:flex;align-items:center;justify-content:center}
.auth.login{left:878px;width:84px}
.auth.signup{left:970px;width:84px}

/* categories */
.categories{left:0;top:104px;width:1200px;height:74px;background:var(--orange)}
.cat{top:0;height:74px;display:flex;flex-direction:column;align-items:center;justify-content:flex-start;padding-top:6px;color:var(--white);font-weight:700;font-size:16px;letter-spacing:.3px}
.cat svg{width:34px;height:34px;margin-bottom:4px;fill:none;stroke:var(--white);stroke-width:2;stroke-linecap:round;stroke-linejoin:round}
.cat-divider{top:0;width:1px;height:74px;background:#e2a17b}

/* results */
.results-title{left:136px;top:228px;font-size:28px;font-weight:400;color:var(--ink)}
.toolbar{top:231px;display:flex;align-items:center;font-size:15px;color:#333}
.field{border:1px solid #cfcfcf;height:28px;display:flex;align-items:center;padding:0 8px;font-size:14px;color:#888;margin-left:5px}
.view-toggle{display:flex;margin-left:10px}
.view-toggle span{width:30px;height:28px;border:1px solid #cfcfcf;display:flex;align-items:center;justify-content:center}
.view-toggle span.on{background:var(--blue);border-color:var(--blue)}
.sort .field{width:71px;justify-content:space-between;font-size:12px}

.note{top:288px;width:205px;height:212px;background:linear-gradient(170deg,var(--note-light),var(--note) 55%,#f0d985);border-radius:2px 2px 12px 30px / 2px 2px 10px 16px;box-shadow:0 8px 8px -4px rgba(0,0,0,.35),inset -3px -3px 10px rgba(180,140,40,.25)}
.avatar{left:63px;top:18px;width:80px;height:80px;border-radius:50%;border:3px solid var(--navy);background:radial-gradient(circle at 50% 40%,#c9a48a,#7a6a5c 70%,#4a4d52)}
.details{left:0;top:110px;width:205px;text-align:center;font-family:"Open Sans",sans-serif;font-size:11px;line-height:19.5px;color:#222}
.details .k{color:#6a6450}

.pager{top:552px;height:38px;width:114px;display:flex;align-items:center;justify-content:center;color:var(--white);font-family:"Open Sans",sans-serif;font-size:17px}
.pager.prev{left:459px;background:linear-gradient(#1f86d2,#145fa3)}
.pager.next{left:581px;background:linear-gradient(#f7803a,var(--orange-dark))}

/* footer */
.site-footer{left:0;top:633px;width:1200px;height:252px;background:var(--footer)}
.foot-col{top:684px;color:var(--white)}
.foot-col h3{font-family:"Montserrat",sans-serif;font-weight:400;font-size:18px;margin-bottom:14px;letter-spacing:-.2px}
.foot-col li{list-style:none;font-size:12.5px;line-height:24px;color:#e6e6e6}
.foot-divider{top:682px;width:1px;height:154px;background:var(--footer-line)}
.follow p{font-size:12.5px;color:#e6e6e6;margin-top:-2px}
.socials{display:flex;gap:28px;margin-top:22px;margin-left:6px}
.socials span{width:18px;height:18px;border-radius:50%;background:var(--white)}
.store-badge{left:898px;width:149px;height:48px;background:#000;border:1px solid #555;border-radius:6px}
.copyright{left:0;top:885px;width:1200px;height:67px;background:var(--footer-bottom);color:#dcdcdc;font-size:12.5px;display:flex;align-items:center;justify-content:center}
</style>
</head>
<body>

<header class="abs site-header">
  <div class="abs brand"><span class="brand-mark"></span><span class="brand-name">Kx7Orbit</span></div>
  <div class="abs lang-switch"><span>Choose Language</span><span class="ar" lang="ar">عربي</span></div>
  <nav class="abs main-nav">
    <a href="#">Home</a><a href="#">Find a Tutor</a><a href="#">About Us</a><a href="#">Contact Us</a>
  </nav>
  <a class="abs auth login">Log In</a>
  <a class="abs auth signup">Sign Up</a>
</header>

<nav class="abs categories">
  <div class="abs cat" style="left:150px;width:120px">
    <svg viewBox="0 0 34 34"><path d="M3 11 17 5l14 6-14 6z" fill="#fff"/><path d="M9 14v7c4 3 12 3 16 0v-7"/><path d="M7 12v12"/></svg>ACADEMIC</div>
  <div class="abs cat-divider" style="left:270px"></div>
  <div class="abs cat" style="left:270px;width:96px">
    <svg viewBox="0 0 34 34"><path d="M12 25V8l15-3v17"/><circle cx="9" cy="25" r="3.5" fill="#fff"/><circle cx="24" cy="22" r="3.5" fill="#fff"/></svg>MUSIC</div>
  <div class="abs cat-divider" style="left:366px"></div>
  <div class="abs cat" style="left:366px;width:68px">
    <svg viewBox="0 0 34 34"><rect x="5" y="7" width="24" height="16" rx="1" fill="#fff"/><path d="M17 23v5M11 28h12"/></svg>I.T.</div>
  <div class="abs cat-divider" style="left:434px"></div>
  <div class="abs cat" style="left:434px;width:141px">
    <svg viewBox="0 0 34 34"><circle cx="17" cy="17" r="12"/><ellipse cx="17" cy="17" rx="5" ry="12"/><path d="M5 17h24M7 11h20M7 23h20"/></svg>LANGUAGES</div>
  <div class="abs cat-divider" style="left:575px"></div>
  <div class="abs cat" style="left:575px;width:119px">
    <svg viewBox="0 0 34 34"><rect x="4" y="11" width="26" height="17" rx="2" fill="#fff"/><path d="M13 11V8h8v3"/><path d="M4 18h26" stroke="#f36f21"/></svg>BUSINESS</div>
  <div class="abs cat-divider" style="left:694px"></div>
  <div class="abs cat" style="left:694px;width:103px">
    <svg viewBox="0 0 34 34"><path d="M10 30l3-12c1-6 6-12 13-14l2 3c-5 2-9 6-10 12l-4 11z"/><path d="M15 14l8 2"/></svg>DANCE</div>
  <div class="abs cat-divider" style="left:797px"></div>
  <div class="abs cat" style="left:797px;width:105px">
    <svg viewBox="0 0 34 34"><circle cx="17" cy="17" r="13"/><path d="M17 11l5 4-2 6h-6l-2-6z" fill="#fff"/></svg>SPORTS</div>
  <div class="abs cat-divider" style="left:902px"></div>
  <div class="abs cat" style="left:902px;width:164px">
    <svg viewBox="0 0 34 34"><path d="M6 4l22 26M28 4 6 30"/><path d="M4 8l4-4M30 8l-4-4"/></svg>ART &amp; CRAFTS</div>
</nav>

<main>
  <h1 class="abs results-title">Search Result</h1>
  <div class="abs toolbar" style="left:619px">Result Count:<span class="field" style="width:44px">04</span></div>
  <div class="abs toolbar" style="left:770px">View Type:
    <div class="view-toggle">
      <span><svg width="10" height="9" viewBox="0 0 10 9"><path d="M0 1h2M4 1h6M0 4.5h2M4 4.5h6M0 8h2M4 8h6" stroke="#1a78c2"/></svg></span>
      <span class="on"><svg width="9" height="9" viewBox="0 0 9 9" fill="#fff"><rect x="0" y="0" width="2" height="2"/><rect x="3.5" y="0" width="2" height="2"/><rect x="7" y="0" width="2" height="2"/><rect x="0" y="3.5" width="2" height="2"/><rect x="3.5" y="3.5" width="2" height="2"/><rect x="7" y="3.5" width="2" height="2"/><rect x="0" y="7" width="2" height="2"/><rect x="3.5" y="7" width="2" height="2"/><rect x="7" y="7" width="2" height="2"/></svg></span>
    </div>
  </div>
  <div class="abs toolbar sort" style="left:928px">Sort By:<span class="field">Name<svg width="8" height="5" viewBox="0 0 8 5"><path d="M0 0h8L4 5z" fill="#666"/></svg></span></div>

  <article class="abs note" style="left:133px">
    <div class="abs avatar" role="img" aria-label="Tutor profile photo"></div>
    <div class="abs details"><span class="k">Username:</span> ramid11<br><span class="k">User Name:</span> Rami Dalton<br><span class="k">Date of Birth:</span> 25 March 1984<br><span class="k">Phone:</span> (555)-204-7316</div>
  </article>
  <article class="abs note" style="left:370px">
    <div class="abs avatar" role="img" aria-label="Tutor profile photo"></div>
    <div class="abs details"><span class="k">Username:</span> ramid11<br><span class="k">User Name:</span> Rami Dalton<br><span class="k">Date of Birth:</span> 25 March 1984<br><span class="k">Phone:</span> (555)-204-7316</div>
  </article>
  <article class="abs note" style="left:610px">
    <div class="abs avatar" role="img" aria-label="Tutor profile photo"></div>
    <div class="abs details"><span class="k">Username:</span> ramid11<br><span class="k">User Name:</span> Rami Dalton<br><span class="k">Date of Birth:</span> 25 March 1984<br><span class="k">Phone:</span> (555)-204-7316</div>
  </article>
  <article class="abs note" style="left:847px">
    <div class="abs avatar" role="img" aria-label="Tutor profile photo"></div>
    <div class="abs details"><span class="k">Username:</span> ramid11<br><span class="k">User Name:</span> Rami Dalton<br><span class="k">Date of Birth:</span> 25 March 1984<br><span class="k">Phone:</span> (555)-204-7316</div>
  </article>

  <a class="abs pager prev">Previous</a>
  <a class="abs pager next">Next</a>
</main>

<footer>
  <div class="abs site-footer"></div>
  <div class="abs foot-col" style="left:144px"><h3>INFORMATION</h3><ul><li>Home</li><li>About Us</li><li>Our Coures</li><li>Admission</li></ul></div>
  <div class="abs foot-divider" style="left:283px"></div>
  <div class="abs foot-col" style="left:322px"><h3>COURSES</h3><ul><li>Mauris vel lacus</li><li>Aitae felis</li><li>Vestibulum</li><li>volutpat imperdiet</li></ul></div>
  <div class="abs foot-divider" style="left:450px"></div>
  <div class="abs foot-col" style="left:490px"><h3>RESOURCES</h3><ul><li>Student Stories</li><li>Our Management</li><li>Our Teachers</li><li>Sitemap</li></ul></div>
  <div class="abs foot-divider" style="left:634px"></div>
  <div class="abs foot-col follow" style="left:670px;top:680px"><h3>FOLLOW US</h3><p>Please connect with us on</p>
    <div class="socials"><span aria-label="Social link 1"></span><span aria-label="Social link 2"></span><span aria-label="Social link 3"></span><span aria-label="Social link 4"></span></div>
  </div>
  <div class="abs foot-divider" style="left:858px;height:160px"></div>
  <div class="abs store-badge" style="top:682px" aria-label="App download badge"></div>
  <div class="abs store-badge" style="top:744px" aria-label="App download badge"></div>
  <div class="abs copyright">© 2016 Company Name&nbsp; All right reserved&nbsp; Term of Use</div>
</footer>

</body>
</html>
```